Builders Worksite Corflute Outdoor Sign

We are a building company who are just branching out into new construction. How first new build is our own home which was designed by us and a local architect. We are proud and want to create more advertisement around our business.

We need a corflute sign that can staked outside the construction site and can be seen by people passing by.
Updates

Can we please make the company name and logo bigger (Tidewater Lane Homes) This needs to be the focus. Can we please replace 'Mako' with 'Contact Us on 021-649-3157'

Target Market(s)

Home owners and people wishing to build on lifestyle blocks in New Zealand.

Font styles to use
Sans Serif

Requirements
Must have
• It needs to feature our:
Logo
Company name
Contact name and number - Mako - 0216493157
Landscape NOT portrait.

```html
<!DOCTYPE html>
<html lang="en">
<head>
<meta charset="utf-8">
<title>Tidewater Lane Homes – Site Sign</title>
<link rel="stylesheet" href="https://fonts.googleapis.com/css2?family=Jost:wght@400&family=League+Spartan:wght@800;900&display=swap">
<style>
  :root {
    --backdrop: #d6d6d6;
    --sign-yellow: #fdd20c;
    --sign-yellow-light: #fff200;
    --sign-navy: #1a2335;
    --sign-white: #ffffff;
  }
  * { box-sizing: border-box; margin: 0; padding: 0; }
  html, body {
    width: 1200px;
    height: 1000px;
    overflow: hidden;
    background: var(--backdrop);
  }
  .sign {
    position: absolute;
    left: 60px;
    top: 95px;
    width: 1080px;
    height: 810px;
    display: grid;
    grid-template-columns: 270px 1fr;
    grid-template-rows: 405px 405px;
    box-shadow: 0 10px 24px rgba(0,0,0,0.25);
  }
  .brand-band {
    grid-column: 1 / 3;
    background: linear-gradient(110deg, var(--sign-yellow-light) 0%, var(--sign-yellow) 45%, var(--sign-yellow) 100%);
    display: flex;
    flex-direction: column;
    align-items: center;
    justify-content: center;
    font-family: "Jost", "Futura", sans-serif;
    font-weight: 400;
    color: var(--sign-navy);
    padding-bottom: 20px;
  }
  .brand-name {
    font-size: 104px;
    line-height: 1;
    letter-spacing: 0.01em;
    text-transform: uppercase;
  }
  .brand-sub {
    margin-top: 50px;
    font-size: 78px;
    line-height: 1;
    letter-spacing: 0.72em;
    margin-right: -0.72em;
    text-transform: uppercase;
  }
  .mark-panel {
    background: var(--sign-white);
    display: flex;
    align-items: center;
    justify-content: center;
  }
  .mark-dot {
    width: 150px;
    height: 150px;
    border-radius: 50%;
    background: var(--sign-navy);
  }
  .contact-panel {
    background: var(--sign-navy);
    display: flex;
    flex-direction: column;
    align-items: center;
    padding-top: 72px;
    font-family: "League Spartan", "Futura", sans-serif;
  }
  .phone-icon {
    width: 88px;
    height: 88px;
  }
  .contact-label {
    margin-top: 34px;
    font-size: 60px;
    font-weight: 800;
    line-height: 1;
    color: var(--sign-yellow);
    text-transform: uppercase;
    letter-spacing: 0.01em;
  }
  .contact-number {
    margin-top: 16px;
    font-size: 90px;
    font-weight: 900;
    line-height: 1;
    color: var(--sign-white);
    letter-spacing: 0.02em;
  }
</style>
</head>
<body>
  <main class="sign">
    <header class="brand-band">
      <h1 class="brand-name">Tidewater Lane</h1>
      <p class="brand-sub">Homes</p>
    </header>
    <div class="mark-panel">
      <div class="mark-dot"></div>
    </div>
    <section class="contact-panel">
      <svg class="phone-icon" viewBox="0 0 88 88" aria-hidden="true">
        <circle cx="44" cy="44" r="44" fill="var(--sign-yellow)"/>
        <path d="M30 22 l8 11 -5 5 c3 7 9 13 16 16 l5 -5 11 8 -5 8 c-20 -1 -37 -18 -38 -38 z" fill="var(--sign-navy)"/>
        <path d="M40 19 l6 7 M62 45 l7 6" stroke="var(--sign-navy)" stroke-width="4" stroke-linecap="round"/>
      </svg>
      <p class="contact-label">Contact us on</p>
      <p class="contact-number">021-649-3157</p>
    </section>
  </main>
</body>
</html>
```